Computer background screen

I've attached our current background I'm looking for a new designs We can use. check out our website and social media for ideas. www.brindlecrestworks.com

Requirements
Must have
• NEED WASHINGTON DC SKYLINE IN PICTURE W/ LOGO

```html
<!DOCTYPE html>
<html lang="en">
<head>
<meta charset="utf-8">
<title>Brindlecrest Works – Desktop Background</title>
<link href="https://fonts.googleapis.com/css2?family=Bebas+Neue&family=Jost:wght@500&display=swap" rel="stylesheet">
<style>
  :root {
    --page: #ffffff;
    --screen: #000000;
    --glow-light: #3a4cff;
    --glow-mid: #121a9a;
    --glow-deep: #05062e;
    --wordmark: #ffffff;
  }
  html, body {
    margin: 0;
    padding: 0;
    width: 1200px;
    height: 1000px;
    overflow: hidden;
    background: var(--page);
  }
  .canvas {
    position: relative;
    width: 1200px;
    height: 1000px;
    background: var(--page);
  }
  .wallpaper {
    position: absolute;
    left: 213px;
    top: 280px;
    width: 799px;
    height: 453px;
    background: var(--screen);
    overflow: hidden;
  }
  .hero-photo {
    position: absolute;
    left: 0;
    top: 0;
    width: 600px;
    height: 453px;
    background: radial-gradient(ellipse 340px 300px at 130px 230px,
      var(--glow-light) 0%, var(--glow-mid) 40%, var(--glow-deep) 75%, var(--screen) 100%);
  }
  .wordmark {
    position: absolute;
    left: 512px;
    top: 0;
    width: 0;
    margin: 0;
    font-weight: 400;
    color: var(--wordmark);
  }
  .wordmark-line,
  .wordmark-suffix {
    position: absolute;
    left: 0;
    transform: translateX(-50%);
    white-space: nowrap;
    text-align: center;
  }
  .wordmark-line {
    font-family: "Bebas Neue", "Oswald", sans-serif;
    font-size: 81px;
    line-height: 81px;
    letter-spacing: 1px;
  }
  .wordmark-line--first { top: 118px; }
  .wordmark-line--second { top: 198px; }
  .wordmark-suffix {
    top: 292px;
    font-family: "Jost", "Futura", sans-serif;
    font-weight: 500;
    font-size: 21px;
    line-height: 30px;
    letter-spacing: 10px;
    padding-left: 10px;
  }
</style>
</head>
<body>
  <main class="canvas">
    <section class="wallpaper">
      <div class="hero-photo" role="img" aria-label="Photograph of an LED spotlight bulb glowing deep blue, with its reflection below"></div>
      <h1 class="wordmark">
        <span class="wordmark-line wordmark-line--first">Brindlecrest</span>
        <span class="wordmark-line wordmark-line--second">Works</span>
        <span class="wordmark-suffix">INCORPORATED</span>
      </h1>
    </section>
  </main>
</body>
</html>
```